Wine Shop Banners

Banner graphic/images required
Require banner images to match the present online wine shop.

www.korbel-traube-laden.de

The wine-shop presently has a very clean, simple design, lots of white space, which is very much the trend at the moment.

Requirements
Images or graphic design for present banners visible on the homepage

The colour and feeling of the banners must fit in with the present clean, simple design.

Work required
3 large slide-card/banners (can be more) and 3 smaller fixed banners below. Please view website to see present position of banners.

LARGE BANNERS x 3

Something special with white background within the banner space
White background on each slide-card. Small individual graphic image in the middle of the slide card. This could be either a simple element of wine:
ingredients, fruit (grape), bottle, cork, old bottle label etc. just displaying one item on each slide-card. Preferably with high quality graphic features.

Note:
We are trying the steer away from the classic stereotype wineshop design. The image/s should have a higher, individual graphic touch, which gives the design something different. Sometimes such artistic work is displayed in steampunk or even in nostalgic design, which leaves the viewer slightly memorized with the content.
To clarify: we are not looking for a full steampunk design but possibly certain elements of this will give you an idea what we mean. That is to say, the design can go slightly in this direction without going over the top. Something small but very eye-catching.

SMALLER BANNERS x 3

One idea is:
Showing a symbol e.g. - discount sign "%" against a white background but again with a high graphic quality.

Target Market(s)

People interested in purchasing wine.
Ages approx. 25 to 65

Industry/Entity Type

Shop

Requirements
Must have
• Something special with white background
• Small individual graphic image in the middle of the slide card.
Nice to have
• The image/s should have a higher, individual graphic touch, which gives the design something different. Something that leaves the viewer slightly memorized with the content.
Should not have
• Not the typical classical design that is often seen on wine shops.

```html
<!DOCTYPE html>
<html lang="en">
<head>
<meta charset="utf-8">
<title>Free Shipping Banner</title>
<link rel="stylesheet" href="https://fonts.googleapis.com/css2?family=Tinos&family=Cinzel:wght@900&display=swap">
<style>
  :root {
    --page: #ffffff;
    --panel-edge: #efefef;
    --panel-center: #ffffff;
    --headline: #4f8a44;
    --headline-dark: #2f5e2a;
    --tag-orange: #f7962f;
    --tag-orange-light: #fdc58a;
    --price-white: #ffffff;
  }
  html, body {
    margin: 0;
    padding: 0;
    width: 1200px;
    height: 900px;
    overflow: hidden;
    background: var(--page);
  }
  .banner {
    position: relative;
    width: 1200px;
    height: 900px;
  }
  .banner-panel {
    position: absolute;
    left: 60px;
    top: 140px;
    width: 1080px;
    height: 500px;
    background: radial-gradient(ellipse 70% 65% at 50% 50%, var(--panel-center) 60%, var(--panel-edge) 100%);
  }
  .headline {
    position: absolute;
    width: 1200px;
    margin: 0;
    text-align: center;
    font-family: "Tinos", "Times New Roman", serif;
    font-weight: 400;
    font-size: 98px;
    line-height: 1;
    white-space: nowrap;
    color: var(--headline);
    text-shadow:
      1px 1px 0 var(--headline-dark),
      2px 3px 4px rgba(0,0,0,0.35);
  }
  .headline-top { top: 168px; left: 6px; }
  .headline-bottom { top: 283px; left: -5px; }
  .price-tag-art {
    position: absolute;
    left: 228px;
    top: 398px;
    width: 752px;
    height: 230px;
    background: linear-gradient(90deg, var(--tag-orange) 0%, var(--tag-orange) 75%, var(--tag-orange-light) 88%, var(--tag-orange) 100%);
  }
  .price {
    position: absolute;
    left: 392px;
    top: 472px;
    margin: 0;
    font-family: "Cinzel", "Times New Roman", serif;
    font-weight: 900;
    font-size: 100px;
    line-height: 1;
    letter-spacing: 18px;
    word-spacing: 40px;
    white-space: nowrap;
    color: var(--price-white);
    text-shadow:
      1px 1px 0 #c9c9c9,
      3px 4px 4px rgba(0,0,0,0.45);
  }
</style>
</head>
<body>
<main class="banner">
  <div class="banner-panel"></div>

  <h1 class="headline headline-top">FREE SHIPPING</h1>
  <p class="headline headline-bottom">ON ORDER OVER</p>

  <div class="price-tag-art" role="img" aria-label="Torn orange paper strip with its right end peeling up in a curl"></div>

  <p class="price">20 $</p>
</main>
</body>
</html>
```